Velmora Trade Hall (front page)

We need a design of a front page for our Velmora Trade Hall website (vth.co.uk). Our company is based in the United Kingdom and offers investors from all over the world an opportunity to invest into bitcoin and litecoin.

We have been developing this cutting edge technology for past 2 years based on our in depth knowledge on conventional stock and currency trading technology and methodology. We have run many test against penetration, security and stability and now are ready to deploy.

Recent news about vulnerability of such platforms leave a great deal of unease from retail investors about investing into cryptocurrency. We are set to challenge this attitude. Our background is payments in particular regulated environment in the UK. We are keen to apply our wealth of experience to provide secure and reliable trading platform and advance cryptocurrency as means of legal tender.

The front page should be based on the feel and look of our current technology vth.co.uk. Some of you have already been involved in logo design for our company, please see the attached mockups. The page should have this minimalist design, very clean and light.

Seek inspiration form www.korvelin.net, www.trusmarq.com, vip.plomwerth.com and other bitcoin exchanges.

We look forward to receiving your ideas.

You can also refer to our social pages:
https://www.facebook.com/vth.co.uk
https://twitter.com/vth_uk

We would like you to focus your efforts at designing the page in such a way so that it is very easy for visitor be open an account with the exchange. We must focus at informing the visitor about the bitcoin, how to my buy, how to sell, look at the general overview of the maker and CONVERTING him/her sing up. This is the most important!!

Regards,
Oren

Reason: Dear all, We are very keen on getting this design done right the first time. The key success is conversion of visitors to subscribers and then to traders. It is absolutely essential make the registration process as streamlined as possible! When we are calling them to act by "Change the world one bitcoin at a time" we should give them a opportunity to provide us with relevant account creation details: email, password, confirm password. Please visit quenzo.co.uk for ideas. Secondly, tell them what is a bitcoin, why a bitcoin is a good investment and how to invest. Finally, it is important to inform visitors of "who we are", what sets us apart from other exchanges, tell them about our experience. In our view graphs and live order books are important but they might turn some visitors away especially the ones that are not accustomed to online trading. Think of what would you like to see on the page if you wanted YOURSELF to invest. What would make you to create an account and use it? Think what will work, we are here to revolutionise how people do business.... any wild ideas put them to us. OUR BUDGET JUST GONE UP!!!

Target Market(s)

A combination of professional and consumer bitcoin investors.

Requirements
Must have
• News section

```html
<!DOCTYPE html>
<html lang="en">
<head>
<meta charset="utf-8">
<title>Velmora Trade Hall – Overview</title>
<link href="https://fonts.googleapis.com/css2?family=Open+Sans:wght@400;600;700&family=Raleway:wght@300;400;600&family=Michroma&display=swap" rel="stylesheet">
<style>
:root{
  --bg-light:#ececec;
  --white:#ffffff;
  --ink:#444444;
  --muted:#8a8a8a;
  --rule:#dddddd;
  --accent:#1ba6e6;
  --accent-dark:#1390cc;
  --up:#2e8fd6;
  --down:#e0513c;
  --vol:#c8c8c8;
  --footer-bar:#3b3b3b;
  --footer:#2c2c2c;
  --footer-text:#bdbdbd;
}
*{box-sizing:border-box;margin:0;padding:0}
html,body{width:688px;height:1200px;overflow:hidden}
body{font-family:"Open Sans",Arial,sans-serif;color:var(--ink);background:var(--white);position:relative}

/* Overview */
.overview{position:absolute;left:0;top:0;width:688px;height:350px;background:var(--bg-light)}
.overview__title{position:absolute;left:16px;top:8px;font-family:"Raleway",sans-serif;font-weight:300;font-size:26px;letter-spacing:2px;color:#555}
.chart-card{position:absolute;left:16px;top:40px;width:656px;height:198px;background:var(--white);box-shadow:0 1px 3px rgba(0,0,0,.12)}
.chart-card__ranges{position:absolute;left:10px;top:8px;display:flex;gap:2px}
.chart-card__ranges span{font-size:6px;border:1px solid var(--rule);padding:1px 3px;color:var(--muted)}
.chart-card__ranges span.is-active{background:#e6f4fc;color:var(--accent-dark)}
.chart-card__pair{position:absolute;left:0;width:100%;top:8px;text-align:center;font-size:8px;font-weight:700;color:#555}
.chart-card svg{position:absolute;left:0;top:20px}
.chart-tabs{position:absolute;left:0;bottom:0;width:100%;height:20px;display:flex;border-top:1px solid var(--rule)}
.chart-tabs span{flex:1;text-align:center;font-size:6.5px;line-height:20px;color:var(--muted);letter-spacing:.5px}
.chart-tabs span.is-active{color:#333;background:#f7f7f7;font-weight:600}

.orders{position:absolute;left:78px;top:280px;width:532px}
.orders__tabs{display:flex;border:1px solid var(--rule);background:var(--white)}
.orders__tabs span{flex:1;text-align:center;font-size:7px;line-height:16px;color:var(--muted)}
.orders__tabs span.is-active{color:#333}
.orders__head{display:flex;justify-content:space-between;background:var(--white);border:1px solid var(--rule);border-top:0;padding:0 14px;height:18px;align-items:center}
.orders__head span{font-size:6.5px;color:#555}
.orders__caret{position:absolute;left:258px;top:34px;width:0;height:0;border-left:6px solid transparent;border-right:6px solid transparent;border-top:6px solid var(--white)}

/* Live tables */
.live{position:absolute;top:350px;left:0;width:688px;height:302px}
.live__title{position:absolute;top:12px;font-family:"Michroma",sans-serif;font-size:15px;color:var(--accent);letter-spacing:.5px}
.data-table{position:absolute;top:50px;border-collapse:collapse;font-size:6.5px;color:#555;background:var(--white)}
.data-table th{font-weight:600;text-align:left;padding:0 8px;height:24px;border-bottom:1px solid var(--rule);color:#333}
.data-table td{padding:0 8px;height:24px;border-bottom:1px solid #efefef}
.trades{left:60px;width:250px}
.book{left:367px;width:272px}

/* News */
.news{position:absolute;top:652px;left:0;width:688px;height:310px;background:var(--accent);color:var(--white)}
.news__title{position:absolute;left:60px;top:22px;font-family:"Raleway",sans-serif;font-weight:400;font-size:22px;letter-spacing:1.5px}
.news__more{position:absolute;right:60px;top:20px;display:flex;align-items:center;gap:5px;font-size:7px;font-weight:600}
.news__more i{display:block;width:12px;height:12px;background:var(--white)}
.news-item{position:absolute;left:60px;width:570px;height:60px}
.news-item__author{position:absolute;left:0;top:2px;font-size:8px}
.news-item__date{position:absolute;left:0;top:14px;font-size:7px;font-weight:700}
.news-item__body{position:absolute;left:145px;top:0;width:425px}
.news-item__headline{font-size:10px;font-weight:700;margin-bottom:3px}
.news-item__text{font-size:6.5px;line-height:9px;opacity:.92}

/* Language bar */
.languages{position:absolute;top:962px;left:0;width:688px;height:46px;background:var(--footer-bar);display:flex;align-items:center;padding-left:44px}
.languages__title{font-family:"Michroma",sans-serif;font-size:10px;color:var(--white);letter-spacing:1px;margin-right:22px}
.languages ul{list-style:none;display:flex}
.languages li{font-size:8px;color:#d6d6d6;padding:0 8px;border-left:1px solid #666}

/* Footer */
.footer{position:absolute;top:1008px;left:0;width:688px;height:192px;background:var(--footer);color:var(--footer-text)}
.footer-col{position:absolute;top:22px}
.footer-col h3{font-family:"Raleway",sans-serif;font-weight:400;font-size:12px;color:var(--white);margin-bottom:6px}
.footer-col ul{list-style:none}
.footer-col li{font-size:7px;line-height:10px}
.newsletter__input{width:110px;height:14px;background:var(--white);font-size:6px;color:#999;padding:3px 4px;margin-top:2px}
.newsletter__button{width:50px;height:12px;background:var(--accent);color:var(--white);font-size:6.5px;text-align:center;line-height:12px;margin-top:4px}
.social{display:flex;gap:6px;margin-top:2px}
.social span{width:22px;height:22px;border-radius:50%;background:var(--accent)}
.footer__legal{position:absolute;left:60px;right:60px;bottom:0;height:32px;border-top:1px solid #444;text-align:center;font-size:6.5px;line-height:32px;color:#9a9a9a}
.footer__legal span{padding:0 6px;border-left:1px solid #555}
.footer__legal span:first-child{border:0}
</style>
</head>
<body>

<section class="overview">
  <h1 class="overview__title">Overview</h1>
  <div class="chart-card">
    <div class="chart-card__ranges"><span>1H</span><span>6H</span><span class="is-active">1D</span><span>3D</span><span>1W</span><span>2W</span><span>1M</span></div>
    <div class="chart-card__pair">BTC/USD</div>
    <svg width="656" height="158" viewBox="0 0 656 158" aria-label="BTC/USD candlestick chart with volume">
      <g stroke="#eeeeee" stroke-width="1">
        <line x1="40" y1="10" x2="630" y2="10"/><line x1="40" y1="40" x2="630" y2="40"/>
        <line x1="40" y1="70" x2="630" y2="70"/><line x1="40" y1="100" x2="630" y2="100"/>
      </g>
      <g font-family="Open Sans, sans-serif" font-size="6" fill="#999">
        <text x="12" y="13">520</text><text x="12" y="43">510</text><text x="12" y="73">500</text><text x="12" y="103">490</text>
        <text x="130" y="154">28.03 06:00</text><text x="300" y="154">28.03 12:00</text><text x="470" y="154">28.03 18:00</text>
      </g>
      <g fill="var(--vol)">
        <rect x="50" y="128" width="6" height="14"/><rect x="64" y="134" width="6" height="8"/><rect x="78" y="120" width="6" height="22"/><rect x="92" y="130" width="6" height="12"/><rect x="106" y="126" width="6" height="16"/><rect x="120" y="132" width="6" height="10"/><rect x="134" y="116" width="6" height="26"/><rect x="148" y="128" width="6" height="14"/><rect x="162" y="135" width="6" height="7"/><rect x="176" y="124" width="6" height="18"/><rect x="190" y="130" width="6" height="12"/><rect x="204" y="110" width="6" height="32"/><rect x="218" y="126" width="6" height="16"/><rect x="232" y="133" width="6" height="9"/><rect x="246" y="122" width="6" height="20"/><rect x="260" y="129" width="6" height="13"/><rect x="274" y="118" width="6" height="24"/><rect x="288" y="131" width="6" height="11"/><rect x="302" y="125" width="6" height="17"/><rect x="316" y="134" width="6" height="8"/><rect x="330" y="121" width="6" height="21"/><rect x="344" y="128" width="6" height="14"/><rect x="358" y="112" width="6" height="30"/><rect x="372" y="130" width="6" height="12"/><rect x="386" y="126" width="6" height="16"/><rect x="400" y="132" width="6" height="10"/><rect x="414" y="119" width="6" height="23"/><rect x="428" y="127" width="6" height="15"/><rect x="442" y="133" width="6" height="9"/><rect x="456" y="114" width="6" height="28"/><rect x="470" y="128" width="6" height="14"/><rect x="484" y="123" width="6" height="19"/><rect x="498" y="131" width="6" height="11"/><rect x="512" y="117" width="6" height="25"/><rect x="526" y="129" width="6" height="13"/><rect x="540" y="124" width="6" height="18"/><rect x="554" y="108" width="6" height="34"/><rect x="568" y="126" width="6" height="16"/><rect x="582" y="120" width="6" height="22"/><rect x="596" y="130" width="6" height="12"/><rect x="610" y="115" width="6" height="27"/>
      </g>
      <g stroke-width="1">
        <g stroke="var(--down)" fill="var(--down)">
          <line x1="53" y1="52" x2="53" y2="70"/><rect x="50" y="56" width="6" height="10"/>
          <line x1="81" y1="58" x2="81" y2="80"/><rect x="78" y="62" width="6" height="12"/>
          <line x1="109" y1="66" x2="109" y2="86"/><rect x="106" y="70" width="6" height="10"/>
          <line x1="137" y1="70" x2="137" y2="94"/><rect x="134" y="74" width="6" height="14"/>
          <line x1="179" y1="76" x2="179" y2="96"/><rect x="176" y="80" width="6" height="11"/>
          <line x1="207" y1="78" x2="207" y2="104"/><rect x="204" y="82" width="6" height="16"/>
          <line x1="249" y1="82" x2="249" y2="100"/><rect x="246" y="85" width="6" height="10"/>
          <line x1="291" y1="76" x2="291" y2="96"/><rect x="288" y="80" width="6" height="11"/>
          <line x1="333" y1="70" x2="333" y2="92"/><rect x="330" y="74" width="6" height="12"/>
          <line x1="375" y1="76" x2="375" y2="98"/><rect x="372" y="80" width="6" height="12"/>
          <line x1="417" y1="70" x2="417" y2="90"/><rect x="414" y="74" width="6" height="10"/>
          <line x1="459" y1="64" x2="459" y2="86"/><rect x="456" y="68" width="6" height="12"/>
          <line x1="501" y1="58" x2="501" y2="78"/><rect x="498" y="62" width="6" height="10"/>
          <line x1="543" y1="48" x2="543" y2="70"/><rect x="540" y="52" width="6" height="12"/>
          <line x1="585" y1="40" x2="585" y2="60"/><rect x="582" y="44" width="6" height="10"/>
        </g>
        <g stroke="var(--up)" fill="var(--up)">
          <line x1="67" y1="54" x2="67" y2="72"/><rect x="64" y="58" width="6" height="8"/>
          <line x1="95" y1="62" x2="95" y2="82"/><rect x="92" y="66" width="6" height="10"/>
          <line x1="123" y1="68" x2="123" y2="88"/><rect x="120" y="72" width="6" height="9"/>
          <line x1="151" y1="74" x2="151" y2="92"/><rect x="148" y="78" width="6" height="9"/>
          <line x1="165" y1="72" x2="165" y2="90"/><rect x="162" y="76" width="6" height="8"/>
          <line x1="193" y1="80" x2="193" y2="98"/><rect x="190" y="84" width="6" height="8"/>
          <line x1="221" y1="84" x2="221" y2="106"/><rect x="218" y="88" width="6" height="12"/>
          <line x1="235" y1="80" x2="235" y2="100"/><rect x="232" y="84" width="6" height="10"/>
          <line x1="263" y1="80" x2="263" y2="98"/><rect x="260" y="84" width="6" height="9"/>
          <line x1="277" y1="76" x2="277" y2="94"/><rect x="274" y="79" width="6" height="10"/>
          <line x1="305" y1="74" x2="305" y2="92"/><rect x="302" y="77" width="6" height="9"/>
          <line x1="319" y1="70" x2="319" y2="88"/><rect x="316" y="73" width="6" height="9"/>
          <line x1="347" y1="72" x2="347" y2="92"/><rect x="344" y="76" width="6" height="10"/>
          <line x1="361" y1="76" x2="361" y2="96"/><rect x="358" y="80" width="6" height="10"/>
          <line x1="389" y1="78" x2="389" y2="96"/><rect x="386" y="82" width="6" height="9"/>
          <line x1="403" y1="72" x2="403" y2="92"/><rect x="400" y="76" width="6" height="10"/>
          <line x1="431" y1="68" x2="431" y2="88"/><rect x="428" y="72" width="6" height="9"/>
          <line x1="445" y1="64" x2="445" y2="84"/><rect x="442" y="68" width="6" height="10"/>
          <line x1="473" y1="62" x2="473" y2="82"/><rect x="470" y="66" width="6" height="10"/>
          <line x1="487" y1="60" x2="487" y2="78"/><rect x="484" y="63" width="6" height="10"/>
          <line x1="515" y1="54" x2="515" y2="74"/><rect x="512" y="58" width="6" height="10"/>
          <line x1="529" y1="50" x2="529" y2="70"/><rect x="526" y="54" width="6" height="10"/>
          <line x1="557" y1="44" x2="557" y2="66"/><rect x="554" y="48" width="6" height="12"/>
          <line x1="571" y1="40" x2="571" y2="60"/><rect x="568" y="44" width="6" height="10"/>
          <line x1="599" y1="36" x2="599" y2="56"/><rect x="596" y="40" width="6" height="10"/>
          <line x1="613" y1="30" x2="613" y2="52"/><rect x="610" y="34" width="6" height="12"/>
        </g>
      </g>
    </svg>
    <div class="chart-tabs"><span>QUOTES</span><span class="is-active">CANDLES</span><span>DEPTH</span><span>VOLUME</span></div>
  </div>

  <div class="orders">
    <div class="orders__tabs"><span class="is-active">Active orders</span><span>All orders</span><span>Trade history</span></div>
    <div class="orders__head"><span>Order</span><span>Time</span><span>Rate Volume</span><span>Vol Volume</span><span>Price</span></div>
    <span class="orders__caret"></span>
  </div>
</section>

<section class="live">
  <h2 class="live__title" style="left:60px">Live Trades</h2>
  <h2 class="live__title" style="left:367px">Live Order Book</h2>
  <table class="data-table trades">
    <tr><th>Time since</th><th>Amount</th><th>Price</th></tr>
    <tr><td>19 seconds</td><td>0.10000000 BTC</td><td>$499.95</td></tr>
    <tr><td>37 seconds</td><td>0.05000000 BTC</td><td>$499.95</td></tr>
    <tr><td>42 seconds</td><td>0.25000000 BTC</td><td>$499.98</td></tr>
    <tr><td>45 seconds</td><td>0.11728322 BTC</td><td>$500.00</td></tr>
    <tr><td>1 minutes</td><td>0.04320790 BTC</td><td>$500.01</td></tr>
  </table>
  <table class="data-table book">
    <tr><th>Bid</th><th></th><th>Ask</th><th></th></tr>
    <tr><td>306.14797603</td><td>$499.99</td><td>86.25498054</td><td>$501.00</td></tr>
    <tr><td>2.03420000</td><td>$499.96</td><td>5.00000000</td><td>$501.50</td></tr>
    <tr><td>12.50000000</td><td>$499.95</td><td>1.57100012</td><td>$502.20</td></tr>
    <tr><td>0.80000000</td><td>$499.90</td><td>30.00000000</td><td>$503.00</td></tr>
    <tr><td>44.10002300</td><td>$499.85</td><td>0.99000000</td><td>$504.10</td></tr>
  </table>
</section>

<section class="news">
  <h2 class="news__title">News</h2>
  <div class="news__more"><i></i>Read More News</div>

  <article class="news-item" style="top:70px">
    <div class="news-item__author">VTH Support Team</div>
    <div class="news-item__date">18 March, 2014</div>
    <div class="news-item__body">
      <h3 class="news-item__headline">Lorem ipsum dolor sit amet, consectetur adipiscing elit.</h3>
      <p class="news-item__text">Cras venenatis imperdiet metus in congue. Donec nunc arcu, consequat vel vulputate eget, eleifend semper augue. Curabitur sed euismod nulla, eget gravida urna. Nullam a lacus ut purus aliquam consectetur. Etiam non metus sollicitudin, porta neque in, vestibulum nunc. Sed eget malesuada diam.</p>
    </div>
  </article>
  <article class="news-item" style="top:128px">
    <div class="news-item__author">VTH Support Team</div>
    <div class="news-item__date">18 March, 2014</div>
    <div class="news-item__body">
      <h3 class="news-item__headline">Lorem ipsum dolor sit amet, consectetur adipiscing elit.</h3>
      <p class="news-item__text">Cras venenatis imperdiet metus in congue. Donec nunc arcu, consequat vel vulputate eget, eleifend semper augue. Curabitur sed euismod nulla, eget gravida urna. Nullam a lacus ut purus aliquam consectetur. Etiam non metus sollicitudin, porta neque in, vestibulum nunc. Sed eget malesuada diam.</p>
    </div>
  </article>
  <article class="news-item" style="top:186px">
    <div class="news-item__author">VTH Support Team</div>
    <div class="news-item__date">18 March, 2014</div>
    <div class="news-item__body">
      <h3 class="news-item__headline">Lorem ipsum dolor sit amet, consectetur adipiscing elit.</h3>
      <p class="news-item__text">Cras venenatis imperdiet metus in congue. Donec nunc arcu, consequat vel vulputate eget, eleifend semper augue. Curabitur sed euismod nulla, eget gravida urna. Nullam a lacus ut purus aliquam consectetur. Etiam non metus sollicitudin, porta neque in, vestibulum nunc. Sed eget malesuada diam.</p>
    </div>
  </article>
  <article class="news-item" style="top:244px">
    <div class="news-item__author">VTH Support Team</div>
    <div class="news-item__date">18 March, 2014</div>
    <div class="news-item__body">
      <h3 class="news-item__headline">Lorem ipsum dolor sit amet, consectetur adipiscing elit.</h3>
      <p class="news-item__text">Cras venenatis imperdiet metus in congue. Donec nunc arcu, consequat vel vulputate eget, eleifend semper augue. Curabitur sed euismod nulla, eget gravida urna. Nullam a lacus ut purus aliquam consectetur. Etiam non metus sollicitudin, porta neque in, vestibulum nunc. Sed eget malesuada diam.</p>
    </div>
  </article>
</section>

<nav class="languages">
  <span class="languages__title">Change Language</span>
  <ul><li>English</li><li>German</li><li>Russian</li><li>Dutch</li><li>Jewish</li><li>Polish</li><li>Czech</li><li>Italian</li><li>Slovenian</li></ul>
</nav>

<footer class="footer">
  <div class="footer-col" style="left:60px">
    <h3>About Us</h3>
    <ul><li>About VTH</li><li>Contact Us</li><li>Privacy Policy</li><li>Terms of Service</li><li>Legal Notice</li><li>API</li></ul>
  </div>
  <div class="footer-col" style="left:162px">
    <h3>Help Center</h3>
    <ul><li>What is Bitcoin?</li><li>How to buy Bitcoins?</li><li>Why to sell bitcoins?</li><li>FAQ</li></ul>
  </div>
  <div class="footer-col" style="left:276px">
    <h3>Data</h3>
    <ul><li>Overview</li><li>Orderbook</li><li>API</li></ul>
  </div>
  <div class="footer-col newsletter" style="left:366px">
    <h3>Subscribe Newsletter</h3>
    <div class="newsletter__input">Email address</div>
    <div class="newsletter__button">Submit</div>
  </div>
  <div class="footer-col" style="left:520px">
    <h3>Get In Touch With Us</h3>
    <div class="social" role="img" aria-label="Social network links"><span></span><span></span><span></span></div>
  </div>
  <div class="footer__legal"><span>© 2014, All Rights reserved, vth.co.uk</span><span>Privacy Policy</span><span>Terms &amp; Conditions</span><span>Contact Us</span></div>
</footer>

</body>
</html>
```